Cybersecurity Start-Up - Tervalo

We need a power-point design for a new company based in Madrid (Spain) called 'Tervalo'. We aim to provide cybersecurity services to small- medium size companies for whom security is critical but paying big money to huge companies is not affordable.

The final design should communicate several things. As technology company which provides cybersecurity, it should be seen as something modern and futuristic , combined with safety and protection.

The company name Tervalo comes from Tervalosa, an ancient Celtiberian settlement in Spain which is famous for its role in the Celtiberian Wars (130 BC). They fought with Rome for 20 years , while being numerical inferior. And they won several times. When a final siege ocurred after a massive deployment of Rome legions, they held their ground for more than a year without food. When the situation was not longer sustainable, they decided to commit suicide rather than become slaves.

So the vision to hold the ground no matter what, should be communicated too
Updates

Need extra days to review

Requirements
Must have
• Check files attached for the logo of the company

```html
<!DOCTYPE html>
<html lang="en">
<head>
<meta charset="utf-8">
<title>Tervalo – Presentation Template</title>
<link href="https://fonts.googleapis.com/css2?family=Carlito:wght@400;700&display=swap" rel="stylesheet">
<style>
:root{
  --orange:#f0641c;
  --orange-mid:#f58a3c;
  --orange-light:#fbc89a;
  --orange-pale:#fde9d8;
  --navy:#1d2b3c;
  --ink:#333333;
  --grey:#6b6b6b;
  --page:#ffffff;
  --slide:#ffffff;
}
*{margin:0;padding:0;box-sizing:border-box}
html,body{width:1200px;height:2486px;overflow:hidden;background:var(--page)}
body{position:relative;font-family:"Carlito","Calibri",Arial,sans-serif;color:var(--ink)}
.slide{position:absolute;width:473px;height:258px;background:var(--slide);box-shadow:0 2px 8px rgba(0,0,0,.18);overflow:hidden}
.slide.cover{left:120px;top:95px;width:968px;height:538px}
.col-l{left:120px}.col-r{left:615px}
.r1{top:697px}.r2{top:987px}.r3{top:1277px}.r4{top:1565px}.r5{top:1855px}.r6{top:2145px}
.facets{position:absolute;role:img}
.facets-right{right:0;top:0;width:62%;height:100%;background:linear-gradient(100deg,rgba(255,255,255,1) 0%,rgba(253,233,216,.6) 35%,rgba(245,160,90,.55) 75%,rgba(226,128,50,.85) 100%)}
.facets-left{left:0;top:0;width:55%;height:100%;background:linear-gradient(280deg,rgba(255,255,255,1) 0%,rgba(253,233,216,.6) 40%,rgba(240,150,80,.7) 85%,rgba(224,120,45,.9) 100%)}
.brand{font-weight:700;color:var(--navy);letter-spacing:.5px;display:flex;align-items:center;gap:10px;position:absolute}
.brand .dot{width:.55em;height:.55em;border-radius:50%;background:var(--orange)}
.cover .brand{left:125px;top:180px;font-size:68px}
.cover .pres-title{position:absolute;left:163px;top:335px;font-size:31px;color:var(--orange)}
.page-no{position:absolute;right:12px;top:0;width:26px;height:20px;background:var(--orange);color:#fff;font-size:11px;font-weight:700;text-align:center;line-height:20px}
.head{position:absolute;left:12px;top:12px;display:flex;align-items:center;gap:7px}
.head .mark{position:relative;width:22px;height:20px}
.head .mark i{position:absolute;width:14px;height:14px;background:var(--orange-mid)}
.head .mark i:first-child{left:0;top:0;background:var(--orange)}
.head .mark i:last-child{left:7px;top:6px}
.head h2{font-size:19px;font-weight:400;color:var(--orange)}
.mini-brand{position:absolute;right:14px;bottom:10px;font-size:10px;font-weight:700;color:var(--navy)}
.small{font-size:8.5px;color:var(--grey);line-height:1.35}
.photo{position:absolute}
/* content slide */
.content-title{position:absolute;left:105px;top:118px;font-size:22px;color:var(--orange)}
.menu{position:absolute;left:235px;top:62px;width:184px}
.menu li{list-style:none;height:17px;margin-bottom:15px;background:linear-gradient(90deg,var(--orange-pale),var(--orange-mid) 55%,var(--orange));font-size:10px;color:var(--orange);padding-left:18px;line-height:17px}
/* about */
.about-text{position:absolute;left:36px;top:48px;width:400px;font-size:8.5px;color:var(--grey);line-height:1.4}
/* donuts */
.donuts{position:absolute;left:0;right:0;top:78px;display:flex;justify-content:space-around;padding:0 30px}
.donut{text-align:center;width:110px}
.donut .lbl{font-size:11px;color:var(--ink);margin-top:8px}
/* data protection divider */
.divider-title{position:absolute;left:98px;top:115px;font-size:22px;color:var(--orange)}
/* lists */
.lead{position:absolute;left:48px;top:52px;font-size:8.5px;font-weight:700;color:var(--ink)}
.quote{position:absolute;left:48px;top:68px;width:390px;font-size:8px;color:var(--grey);line-height:1.35}
.bullet{position:absolute;display:flex;gap:10px}
.bullet b{display:block;width:9px;height:9px;background:var(--orange);margin-top:2px}
.bullet .t{font-size:10.5px;color:var(--ink)}
.bullet .s{font-size:8px;color:var(--grey)}
/* team */
.team-card{position:absolute;top:14px;width:90px;height:140px;background:rgba(240,120,70,.72);text-align:center;color:#fff}
.team-card .avatar{width:54px;height:54px;border-radius:50%;background:#fff;border:2px solid var(--orange);margin:6px auto 14px}
.team-card .t{font-size:10.5px}
.team-card .s{font-size:8px;opacity:.9}
/* privacy */
.privacy-box{position:absolute;left:320px;top:47px;width:153px;height:176px;background:rgba(240,110,60,.85);color:#fff;padding:14px 14px}
.privacy-box h3{font-size:9px;font-weight:700;margin-bottom:6px}
.privacy-box p{font-size:8px;line-height:1.35;text-align:justify}
/* arrows */
.label{position:absolute;text-align:center;font-size:10.5px;color:var(--ink)}
.label .s{font-size:8px;color:var(--grey)}
/* timeline */
.year{position:absolute;top:153px;text-align:center;width:100px;font-size:8.5px;color:var(--grey);line-height:1.35}
/* contact */
.contact .brand{left:45px;top:60px;font-size:34px}
.contact .heading{position:absolute;left:47px;top:140px;font-size:10px;color:var(--orange);letter-spacing:.3px}
.contact ul{position:absolute;left:47px;top:162px;list-style:none;font-size:11px;color:var(--ink);line-height:1.75}
</style>
</head>
<body>

<!-- Cover -->
<section class="slide cover">
  <div class="facets facets-right" role="img" aria-label="Soft orange faceted geometric background"></div>
  <div class="brand"><span>Tervalo</span><span class="dot"></span></div>
  <div class="pres-title">Presentation Title</div>
</section>

<!-- 2 Content -->
<section class="slide col-l r1">
  <div class="facets facets-left" role="img" aria-label="Soft orange faceted geometric background"></div>
  <span class="page-no">2</span>
  <div class="content-title">Content</div>
  <ul class="menu">
    <li>Lorem ipsum</li><li>Lorem ipsum</li><li>Lorem ipsum</li><li>Lorem ipsum</li><li>Lorem ipsum</li>
  </ul>
</section>

<!-- 3 About Us -->
<section class="slide col-r r1">
  <div class="head"><div class="mark"><i></i><i></i></div><h2>About Us</h2></div>
  <span class="page-no">3</span>
  <p class="about-text">Lorem Ipsum is simply dummy text of the printing and typesetting industry. Lorem Ipsum has been the industry's standard dummy text ever since the 1500s, when an unknown printer took a galley of type and scrambled it to make a type specimen book.</p>
  <div class="photo" role="img" aria-label="Photo of a padlock resting on a laptop keyboard" style="left:0;top:98px;width:473px;height:160px;background:linear-gradient(100deg,#44607e 0%,#8aa1b8 35%,#c9d4de 60%,#eef1f4 100%)"></div>
  <span class="mini-brand">Tervalo</span>
</section>

<!-- 4 Column Chart -->
<section class="slide col-l r2">
  <div class="head"><div class="mark"><i></i><i></i></div><h2>Column Chart</h2></div>
  <span class="page-no">4</span>
  <svg style="position:absolute;left:70px;top:78px" width="290" height="140" viewBox="0 0 290 140" font-family="Carlito, sans-serif" font-size="8" fill="#555">
    <g stroke="#ddd" stroke-width="1">
      <line x1="20" y1="10" x2="280" y2="10"/><line x1="20" y1="30" x2="280" y2="30"/><line x1="20" y1="50" x2="280" y2="50"/>
      <line x1="20" y1="70" x2="280" y2="70"/><line x1="20" y1="90" x2="280" y2="90"/><line x1="20" y1="110" x2="280" y2="110"/>
    </g>
    <text x="8" y="113">0</text><text x="8" y="93">1</text><text x="8" y="73">2</text><text x="8" y="53">3</text><text x="8" y="33">4</text><text x="8" y="13">5</text>
    <g>
      <rect x="30" y="24" width="11" height="86" fill="#e35a1a"/><rect x="43" y="62" width="11" height="48" fill="#f8c28f"/><rect x="56" y="70" width="11" height="40" fill="#f08a3c"/>
      <rect x="92" y="60" width="11" height="50" fill="#e35a1a"/><rect x="105" y="22" width="11" height="88" fill="#f8c28f"/><rect x="118" y="70" width="11" height="40" fill="#f08a3c"/>
      <rect x="154" y="40" width="11" height="70" fill="#e35a1a"/><rect x="167" y="74" width="11" height="36" fill="#f8c28f"/><rect x="180" y="50" width="11" height="60" fill="#f08a3c"/>
      <rect x="216" y="20" width="11" height="90" fill="#e35a1a"/><rect x="229" y="54" width="11" height="56" fill="#f8c28f"/><rect x="242" y="10" width="11" height="100" fill="#f08a3c"/>
    </g>
    <text x="32" y="126">Category 1</text><text x="94" y="126">Category 2</text><text x="156" y="126">Category 3</text><text x="218" y="126">Category 4</text>
  </svg>
  <span class="mini-brand">Tervalo</span>
</section>

<!-- 5 Donuts -->
<section class="slide col-r r2">
  <div class="head"><div class="mark"><i></i><i></i></div><h2>Column Chart</h2></div>
  <span class="page-no">5</span>
  <div class="donuts">
    <div class="donut">
      <svg width="86" height="86" viewBox="0 0 86 86"><circle cx="43" cy="43" r="36" fill="none" stroke="#f8a461" stroke-width="10"/><circle cx="43" cy="43" r="36" fill="none" stroke="#e85a1a" stroke-width="10" stroke-dasharray="68 158" transform="rotate(-90 43 43)"/><text x="43" y="48" text-anchor="middle" font-size="16" fill="#444" font-family="Carlito, sans-serif">30%</text></svg>
      <div class="lbl">Lorem ipsum</div><div class="small">Lorem Ipsum is<br>simply dummy text</div>
    </div>
    <div class="donut">
      <svg width="86" height="86" viewBox="0 0 86 86"><circle cx="43" cy="43" r="36" fill="none" stroke="#f8a461" stroke-width="10"/><circle cx="43" cy="43" r="36" fill="none" stroke="#e85a1a" stroke-width="10" stroke-dasharray="68 158" transform="rotate(-90 43 43)"/><text x="43" y="48" text-anchor="middle" font-size="16" fill="#444" font-family="Carlito, sans-serif">30%</text></svg>
      <div class="lbl">Lorem ipsum</div><div class="small">Lorem Ipsum is<br>simply dummy text</div>
    </div>
    <div class="donut">
      <svg width="86" height="86" viewBox="0 0 86 86"><circle cx="43" cy="43" r="36" fill="none" stroke="#f8a461" stroke-width="10"/><circle cx="43" cy="43" r="36" fill="none" stroke="#e85a1a" stroke-width="10" stroke-dasharray="68 158" transform="rotate(-90 43 43)"/><text x="43" y="48" text-anchor="middle" font-size="16" fill="#444" font-family="Carlito, sans-serif">30%</text></svg>
      <div class="lbl">Lorem ipsum</div><div class="small">Lorem Ipsum is<br>simply dummy text</div>
    </div>
  </div>
  <span class="mini-brand">Tervalo</span>
</section>

<!-- 6 Data Protection divider -->
<section class="slide col-l r3">
  <div class="facets facets-left" role="img" aria-label="Soft orange faceted geometric background"></div>
  <div class="photo" role="img" aria-label="Photo of a silver padlock on a white keyboard" style="left:262px;top:0;width:211px;height:258px;background:linear-gradient(90deg,rgba(255,255,255,0) 0%,#eceff2 25%,#d5dade 60%,#f3f4f6 100%)"></div>
  <span class="page-no">6</span>
  <div class="divider-title">Data Protection</div>
</section>

<!-- 7 Data Management -->
<section class="slide col-r r3">
  <div class="head"><div class="mark"><i></i><i></i></div><h2>Data Management</h2></div>
  <span class="page-no">7</span>
  <div class="lead">The standard Lorem Ipsum passage, used since the 1500s</div>
  <p class="quote">"Lorem ipsum dolor sit amet, consectetur adipiscing elit, sed do eiusmod tempor incididunt ut labore et dolore magna aliqua. Ut enim ad minim veniam, quis nostrud exercitation ullamco laboris nisi ut aliquip ex ea commodo consequat."</p>
  <div class="bullet" style="left:58px;top:130px"><b></b><div><div class="t">Lorem ipsum</div><div class="s">Lorem Ipsum is simply dummy text</div></div></div>
  <div class="bullet" style="left:295px;top:125px"><b></b><div><div class="t">Lorem ipsum</div><div class="s">Lorem Ipsum is simply dummy text</div></div></div>
  <div class="bullet" style="left:58px;top:180px"><b></b><div><div class="t">Lorem ipsum</div><div class="s">Lorem Ipsum is simply dummy text</div></div></div>
  <div class="bullet" style="left:295px;top:178px"><b></b><div><div class="t">Lorem ipsum</div><div class="s">Lorem Ipsum is simply dummy text</div></div></div>
  <span class="mini-brand">Tervalo</span>
</section>

<!-- 8 Data Protection -->
<section class="slide col-l r4">
  <div class="head"><div class="mark"><i></i><i></i></div><h2>Data Protection</h2></div>
  <span class="page-no">8</span>
  <div class="bullet" style="left:58px;top:65px"><b></b><div><div class="t">Lorem ipsum</div><div class="s">Lorem Ipsum is simply dummy text</div></div></div>
  <div class="bullet" style="left:58px;top:115px"><b></b><div><div class="t">Lorem ipsum</div><div class="s">Lorem Ipsum is simply dummy text</div></div></div>
  <div class="bullet" style="left:58px;top:165px"><b></b><div><div class="t">Lorem ipsum</div><div class="s">Lorem Ipsum is simply dummy text</div></div></div>
  <div class="photo" role="img" aria-label="Illustration of a security shield in front of a laptop" style="left:255px;top:70px;width:180px;height:110px;border-radius:8px;background:radial-gradient(ellipse at center,#c9ccd0 0%,#e6e8ea 55%,#ffffff 100%)"></div>
  <span class="mini-brand">Tervalo</span>
</section>

<!-- 9 Our Team -->
<section class="slide col-r r4">
  <div class="head"><div class="mark"><i></i><i></i></div><h2>Our Team</h2></div>
  <span class="page-no">8</span>
  <div class="photo" role="img" aria-label="Photo of a padlock on a laptop keyboard" style="left:0;top:58px;width:473px;height:160px;background:linear-gradient(100deg,#3f5b7a 0%,#8aa1b8 40%,#c7d2dc 70%,#e9eef2 100%)">
    <div class="team-card" style="left:50px"><div class="avatar"></div><div class="t">Lorem ipsum</div><div class="s">simply dummy text</div></div>
    <div class="team-card" style="left:185px"><div class="avatar"></div><div class="t">Lorem ipsum</div><div class="s">simply dummy text</div></div>
    <div class="team-card" style="left:325px"><div class="avatar"></div><div class="t">Lorem ipsum</div><div class="s">simply dummy text</div></div>
  </div>
  <span class="mini-brand">Tervalo</span>
</section>

<!-- 10 Data Privacy -->
<section class="slide col-l r5">
  <div class="head"><div class="mark"><i></i><i></i></div><h2>Data Privacy</h2></div>
  <span class="page-no">10</span>
  <div class="photo" role="img" aria-label="Photo of a keyboard with a blue security key" style="left:0;top:47px;width:330px;height:176px;background:linear-gradient(120deg,#e3e6ea 0%,#c9ced4 40%,#6f8fae 65%,#d7dbe0 100%)"></div>
  <div class="privacy-box">
    <h3>What is Lorem Ipsum?</h3>
    <p>Lorem Ipsum is simply dummy text of the printing and typesetting industry. Lorem Ipsum has been the industry's standard dummy text ever since the 1500s, when an unknown printer took a galley of type and scrambled it to make a type specimen book.</p>
  </div>
  <span class="mini-brand">Tervalo</span>
</section>

<!-- 11 Data Development -->
<section class="slide col-r r5">
  <div class="head"><div class="mark"><i></i><i></i></div><h2>Data Development</h2></div>
  <span class="page-no">11</span>
  <svg style="position:absolute;left:150px;top:68px" width="175" height="190" viewBox="0 0 175 190" fill="#f0641c">
    <rect x="78" y="30" width="18" height="160"/>
    <polygon points="87,0 70,32 104,32"/>
    <path d="M62 190 V88 Q62 70 44 70 H22 V58 L0 76 L22 94 V82 H44 Q50 82 50 88 V190 Z"/>
    <path d="M113 190 V88 Q113 70 131 70 H153 V58 L175 76 L153 94 V82 H131 Q125 82 125 88 V190 Z"/>
  </svg>
  <div class="label" style="left:190px;top:34px;width:95px">Lorem ipsum<div class="s">simply dummy text</div></div>
  <div class="label" style="left:55px;top:120px;width:95px">Lorem ipsum<div class="s">simply dummy text</div></div>
  <div class="label" style="left:330px;top:120px;width:95px">Lorem ipsum<div class="s">simply dummy text</div></div>
  <span class="mini-brand">Tervalo</span>
</section>

<!-- 12 Achievements -->
<section class="slide col-l r6">
  <div class="head"><div class="mark"><i></i><i></i></div><h2>Achivements</h2></div>
  <span class="page-no">12</span>
  <svg style="position:absolute;left:0;top:80px" width="473" height="70" viewBox="0 0 473 70" font-family="Carlito, sans-serif">
    <rect x="0" y="34" width="473" height="10" fill="#f8a461"/>
    <g fill="#fff" stroke="#f0641c" stroke-width="4">
      <circle cx="85" cy="39" r="21"/><circle cx="175" cy="39" r="21"/><circle cx="265" cy="39" r="21"/><circle cx="355" cy="39" r="21"/>
    </g>
    <g fill="#f0641c" font-size="10" text-anchor="middle">
      <text x="85" y="43">2015</text><text x="175" y="43">2016</text><text x="265" y="43">2017</text><text x="355" y="43">2018</text>
    </g>
    <g stroke="#f0641c" stroke-width="2"><line x1="85" y1="6" x2="85" y2="18"/><line x1="175" y1="6" x2="175" y2="18"/><line x1="265" y1="6" x2="265" y2="18"/><line x1="355" y1="6" x2="355" y2="18"/></g>
  </svg>
  <div class="year" style="left:35px">Lorem Ipsum is<br>simply dummy text</div>
  <div class="year" style="left:125px">Lorem Ipsum is<br>simply dummy text</div>
  <div class="year" style="left:215px">Lorem Ipsum is<br>simply dummy text</div>
  <div class="year" style="left:305px">Lorem Ipsum is<br>simply dummy text</div>
  <span class="mini-brand">Tervalo</span>
</section>

<!-- 13 Contact -->
<section class="slide col-r r6 contact">
  <div class="facets facets-right" role="img" aria-label="Soft orange faceted geometric background"></div>
  <div class="brand"><span>Tervalo</span><span class="dot"></span></div>
  <div class="heading">CONTACT DETAILS</div>
  <ul>
    <li>www.Lorem ipsum.com</li>
    <li>Lorem ipsum@emailid.com</li>
    <li>Contact number</li>
  </ul>
</section>

</body>
</html>
```